Consulting firm needs elegant, modern designs

Business card design - I have a logo which has previously been developed for K-Pathways - I will attach. I will also attach specifications for the size of the business card.

We also need a logo design for our leadership consulting product - Frame of Guidance - we focus on improving workplace health by educating leaders and learning professionals about how the physical and emotional affects performance and engagement. I have some example logos and ideas which I will attach - these have attempted to bring in the body but I do not like the font (see www.frameofguidance.example for preferred font). Idea is to please have a 'body' visible somehow in the word Leadership, ensuring that this conveys flexibility and agility. Colors which I prefer are deep purple OR turquoise, together with silver. COLORS below are for LOGO design.

Target Market(s)

For the business card, it should be more masculine. The logo which will be attached should be neutralized into dark blue shades and silver. The business card K-Pathways is focused on business transformation - organizations who would require a consultant to help them enter new markets, for example.

Industry/Entity Type

Leadership

Contact Information for Business Card

Content:
K-Pathways
Molenkade 27
4921KT, Breda, The Netherlands
maarten@K-Pathways.example
www.K-Pathways.example

Colors for business card should be conservative and slightly more masculine. Use the K-Pathways logo but change the colors to blue or shades of gray/black.

Dimensions for cut
85 x 55 mm
1004 x 650 pixels
Full document size
88 x 58 mm
1040 x 685 pixels
For the best result, you need to design the full document size including the bleed

Logo Text

Frame of Guidance

Font styles to use
Serif
Sans Serif

Colors
876aae
333333
959595

Requirements
Must have
• Professional, modern and unique business card design
• Professional, elegant, and modern logo design - with creative thinking
Should not have
• Too many colors

```html
<!DOCTYPE html>
<html lang="en">
<head>
<meta charset="utf-8">
<title>K-Pathways Business Card</title>
<link href="https://fonts.googleapis.com/css2?family=Open+Sans:wght@400;600;700&display=swap" rel="stylesheet">
<style>
  :root {
    --backdrop: #e9e6e2;
    --kraft-light: #ccaa82;
    --kraft: #c19d74;
    --kraft-dark: #b8936a;
    --ink: #141210;
    --ink-soft: #2a241f;
  }
  * { margin: 0; padding: 0; box-sizing: border-box; }
  html, body {
    width: 1200px;
    height: 900px;
    overflow: hidden;
  }
  body {
    position: relative;
    background: var(--backdrop);
    font-family: "Open Sans", Arial, sans-serif;
    color: var(--ink);
  }
  .card {
    position: absolute;
    width: 556px;
    height: 342px;
    background: linear-gradient(135deg, var(--kraft-light) 0%, var(--kraft) 55%, var(--kraft-dark) 100%);
    box-shadow: 0 6px 18px rgba(0,0,0,0.18);
  }
  .card--front { left: 238px; top: 62px; }
  .card--back { left: 458px; top: 518px; width: 560px; }

  /* Front */
  .front-mark {
    position: absolute;
    left: 36px;
    top: 98px;
    width: 210px;
    display: flex;
    align-items: center;
    gap: 10px;
  }
  .front-mark__dot {
    width: 26px; height: 26px;
    border-radius: 50%;
    background: var(--ink);
    flex: none;
  }
  .front-mark__name {
    font-size: 28px;
    font-weight: 700;
    color: var(--ink);
    white-space: nowrap;
  }
  .divider {
    position: absolute;
    left: 255px;
    top: 76px;
    width: 1px;
    height: 190px;
    background: var(--ink-soft);
  }
  .details {
    position: absolute;
    left: 277px;
    top: 73px;
    line-height: 1.25;
  }
  .details__name { font-size: 18px; font-weight: 700; }
  .details__role { font-size: 14.5px; }
  .details__contacts { margin-top: 22px; }
  .contact {
    display: flex;
    align-items: center;
    gap: 7px;
    font-size: 16px;
    height: 22px;
  }
  .contact svg { width: 14px; height: 14px; flex: none; }
  .details__company { margin-top: 18px; font-size: 16.5px; font-weight: 700; }
  .details__address { font-size: 14.5px; line-height: 1.6; }

  /* Back */
  .back-brand__row {
    position: absolute;
    left: 87px;
    top: 140px;
    display: flex;
    align-items: center;
    gap: 16px;
  }
  .back-brand__dot {
    width: 46px; height: 46px;
    border-radius: 50%;
    background: var(--ink);
    flex: none;
  }
  .back-brand__name {
    font-size: 52px;
    font-weight: 600;
    letter-spacing: -0.5px;
    line-height: 1;
    white-space: nowrap;
  }
  .back-brand__tagline {
    position: absolute;
    left: 210px;
    top: 206px;
    font-size: 17px;
    color: var(--ink-soft);
    white-space: nowrap;
  }
</style>
</head>
<body>
  <section class="card card--front">
    <div class="front-mark">
      <span class="front-mark__dot"></span>
      <span class="front-mark__name">K-Pathways</span>
    </div>
    <div class="divider"></div>
    <div class="details">
      <p class="details__name">Pieter Janssen</p>
      <p class="details__role">Managing Director</p>
      <div class="details__contacts">
        <p class="contact">
          <svg viewBox="0 0 14 14" aria-hidden="true"><rect x="1" y="3" width="12" height="9" fill="#141210"/><path d="M1.5 3.5 L7 8 L12.5 3.5" stroke="#c4a077" stroke-width="1.2" fill="none"/></svg>
          maarten@K-Pathways.example
        </p>
        <p class="contact">
          <svg viewBox="0 0 14 14" aria-hidden="true"><circle cx="7" cy="7" r="6" fill="#141210"/><path d="M1 7 H13 M7 1 C4 4 4 10 7 13 M7 1 C10 4 10 10 7 13" stroke="#c4a077" stroke-width="0.9" fill="none"/></svg>
          www.K-Pathways.example
        </p>
      </div>
      <p class="details__company">K-Pathways</p>
      <p class="details__address">Molenkade 27<br>4921KT, Breda, The Netherlands</p>
    </div>
  </section>

  <section class="card card--back">
    <div class="back-brand__row">
      <span class="back-brand__dot"></span>
      <span class="back-brand__name">K-Pathways</span>
    </div>
    <p class="back-brand__tagline">Guiding every stride</p>
  </section>
</body>
</html>
```